Technology Solutions Provider

Let’s design a business card that will be as simple and bold at the same time. Name, email address, website & phone number.

Target Market(s)

Small to Medium Size Business

Industry/Entity Type

It Professional

Contact Information for Business Card

Name, email, website, phone numbers

Font styles to use
Sans Serif

Colors
ec1f27
f04a50
dddddd
919191
000000
ffffff

Requirements
Must have
• Clean simple look using my existing logo. I just need to the basic contact information on this card.
Nice to have
• Im considering the square size card versus the standard size business card.
Should not have
• No Mailing Address, no list of services.

```html
<!DOCTYPE html>
<html lang="en">
<head>
<meta charset="utf-8">
<title>sablenet business card</title>
<link rel="stylesheet" href="https://fonts.googleapis.com/css2?family=Exo+2:wght@400;500&display=swap">
<style>
  :root {
    --brand-red: #dd2427;
    --ink: #111111;
    --muted: #919191;
    --paper: #ffffff;
    --backdrop: #353535;
  }
  * { margin: 0; padding: 0; box-sizing: border-box; }
  html, body { width: 1200px; height: 800px; overflow: hidden; }
  body {
    background: var(--backdrop);
    font-family: "Exo 2", sans-serif;
    position: relative;
  }
  .card {
    position: absolute;
    top: 256px;
    width: 335px;
    height: 318px;
    box-shadow: 0 2px 4px rgba(0,0,0,0.45);
  }
  .card--front { left: 243px; background: var(--paper); }
  .card--back { left: 626px; background: var(--brand-red); }

  .brand {
    position: absolute;
    left: 0; right: 0;
    display: flex;
    flex-direction: column;
    align-items: center;
    line-height: 1;
  }
  .brand__row { display: flex; align-items: center; gap: 8px; }
  .brand__dot { width: 10px; height: 10px; border-radius: 50%; }
  .brand__name { font-weight: 400; letter-spacing: 0.5px; }
  .brand__tagline { margin-top: 4px; font-weight: 400; }

  .card--front .brand { top: 74px; }
  .card--front .brand__name { font-size: 34px; color: var(--brand-red); }
  .card--front .brand__dot { background: var(--brand-red); }
  .card--front .brand__tagline { font-size: 11px; color: var(--muted); }

  .card--back .brand { top: 128px; }
  .card--back .brand__name { font-size: 38px; color: var(--paper); }
  .card--back .brand__dot { background: var(--paper); }
  .card--back .brand__tagline { font-size: 12px; color: var(--paper); }

  .contact {
    position: absolute;
    top: 189px;
    left: 0; right: 0;
    text-align: center;
    color: var(--ink);
  }
  .contact__name {
    font-size: 14.5px;
    font-weight: 500;
    color: var(--brand-red);
    letter-spacing: 0.4px;
    line-height: 17px;
  }
  .contact__role { font-size: 11px; line-height: 13px; }
  .contact__rule {
    width: 100px; height: 1px;
    background: var(--brand-red);
    margin: 9px auto 10px;
  }
  .contact__icons { display: flex; justify-content: center; gap: 3px; height: 11px; margin-bottom: 2px; }
  .contact__icons svg { width: 10px; height: 10px; }
  .contact__line { font-size: 11px; line-height: 13.6px; }
</style>
</head>
<body>
  <section class="card card--front">
    <div class="brand">
      <div class="brand__row">
        <span class="brand__dot"></span>
        <span class="brand__name">sablenet</span>
      </div>
      <span class="brand__tagline">technology solutions provider</span>
    </div>

    <div class="contact">
      <p class="contact__name">MARCUS HALE</p>
      <p class="contact__role">Managing Director</p>
      <div class="contact__rule"></div>
      <div class="contact__icons">
        <svg viewBox="0 0 10 10" aria-label="phone" role="img">
          <rect width="10" height="10" rx="2" fill="var(--brand-red)"/>
          <path d="M3 2.2 L4.2 3.6 L3.6 4.4 Q4.5 5.8 5.6 6.4 L6.4 5.8 L7.8 7 L7 8 Q4.4 7.8 2.2 3 Z" fill="#fff"/>
        </svg>
        <svg viewBox="0 0 10 10" aria-label="email" role="img">
          <rect width="10" height="10" rx="2" fill="var(--brand-red)"/>
          <rect x="2" y="3" width="6" height="4.2" fill="none" stroke="#fff" stroke-width="0.8"/>
          <path d="M2 3 L5 5.4 L8 3" fill="none" stroke="#fff" stroke-width="0.8"/>
        </svg>
        <svg viewBox="0 0 10 10" aria-label="website" role="img">
          <rect width="10" height="10" rx="2" fill="var(--brand-red)"/>
          <circle cx="5" cy="5" r="2.8" fill="none" stroke="#fff" stroke-width="0.8"/>
          <path d="M2.2 5 H7.8 M5 2.2 Q3.6 5 5 7.8 Q6.4 5 5 2.2" fill="none" stroke="#fff" stroke-width="0.6"/>
        </svg>
      </div>
      <p class="contact__line">(071)555018240</p>
      <p class="contact__line">hello@sablenet.com</p>
      <p class="contact__line">www.sablenet-it.com</p>
    </div>
  </section>

  <section class="card card--back">
    <div class="brand">
      <div class="brand__row">
        <span class="brand__dot"></span>
        <span class="brand__name">sablenet</span>
      </div>
      <span class="brand__tagline">technology solutions provider</span>
    </div>
  </section>
</body>
</html>
```